electrical contractor business card for professional modern company

I need a business card design for an electrical contractors business. I do all kinds of electricical work from new homes, air conditioning, data and communications. I have a logo design i want on it and have a good idea in my head of what i want it to look like. I like simple yet bold and professional looking. All black background is a must

Target Market(s)

Anyone needing electrical work done

Industry/Entity Type

Electrical

Contact Information for Business Card

company name- KTW Electrical and Data
person name-martin pellowe
phone number- 0418 362 927
website-ktwelec.example.com.au

Font styles to use
Sans Serif

Requirements
Must have
• email
• website
• logo
• name
• phone number
• list of work i do:
• -electrical
• -air-conditioning
• -data/communications
• -cctv/security
• -domestic/commercial/industrial
• -24hr emergency breakdown repair
Nice to have
• i would like the logo on the front side in the centre taking up most of the card with black background.
• on the rear i want the list of work i do with company info i.e. email, website, my name, phone number. rear of card also black background with orange writing to match the orange in the logo

```html
<!DOCTYPE html>
<html lang="en">
<head>
<meta charset="utf-8">
<title>KTW Electrical and Data – Business Card</title>
<link href="https://fonts.googleapis.com/css2?family=Open+Sans:wght@400;600&display=swap" rel="stylesheet">
<style>
  :root {
    --backdrop: #d6d7d8;
    --card-top: #1c1c1e;
    --card-bottom: #030303;
    --orange: #e3833a;
    --orange-soft: #c9722f;
    --ghost: #3a3b3e;
    --divider: #8a5a32;
  }
  * { box-sizing: border-box; margin: 0; padding: 0; }
  html, body {
    width: 1200px;
    height: 968px;
    overflow: hidden;
  }
  body {
    background: var(--backdrop);
    font-family: "Open Sans", Arial, sans-serif;
    position: relative;
  }
  .card {
    position: absolute;
    width: 640px;
    height: 391px;
    background: linear-gradient(180deg, var(--card-top) 0%, var(--card-bottom) 70%);
    box-shadow: 0 10px 24px rgba(0,0,0,0.35);
    overflow: hidden;
  }
  .card--back { left: 470px; top: 60px; }
  .card--front { left: 90px; top: 510px; }

  /* Back side */
  .contact-name {
    position: absolute;
    left: 120px;
    top: 34px;
    font-size: 42px;
    font-weight: 400;
    color: var(--orange);
    letter-spacing: 0.5px;
  }
  .contact-role {
    position: absolute;
    right: 130px;
    top: 92px;
    font-size: 17px;
    color: var(--orange);
  }
  .services {
    position: absolute;
    left: 82px;
    top: 120px;
    color: var(--orange);
    font-size: 14px;
    line-height: 17px;
  }
  .services__intro { margin-left: 4px; }
  .services__list { list-style: none; }
  .services__list li {
    display: flex;
    align-items: center;
    gap: 7px;
  }
  .services__list li::before {
    content: "";
    width: 9px;
    height: 9px;
    border-radius: 50%;
    background: radial-gradient(circle at 35% 35%, #f4a86a, var(--orange-soft));
    flex: none;
  }
  .ghost-mark {
    position: absolute;
    right: 70px;
    top: 222px;
    font-size: 18px;
    font-weight: 600;
    color: var(--ghost);
  }
  .contact-row {
    position: absolute;
    left: 100px;
    top: 292px;
    display: flex;
    align-items: center;
    color: var(--orange);
    font-size: 17px;
  }
  .contact-row svg { margin-right: 14px; }
  .contact-row__divider {
    width: 1px;
    height: 30px;
    background: var(--divider);
    margin: 0 14px;
  }

  /* Front side */
  .brand {
    position: absolute;
    inset: 0;
    display: flex;
    align-items: center;
    justify-content: center;
    gap: 16px;
  }
  .brand__dot {
    width: 26px;
    height: 26px;
    border-radius: 50%;
    background: var(--orange);
  }
  .brand__name {
    font-size: 34px;
    font-weight: 600;
    color: var(--orange);
  }
</style>
</head>
<body>

  <section class="card card--back" aria-label="Card back">
    <h1 class="contact-name">Martin Pellowe</h1>
    <p class="contact-role">Electrical contractors</p>
    <div class="services">
      <p class="services__intro">I do all kinds of electrical work</p>
      <ul class="services__list">
        <li>electrical</li>
        <li>air-conditioning</li>
        <li>data/communications</li>
        <li>cctv/security</li>
        <li>domestic/commercial/industrial</li>
        <li>24hr emergency breakdown repair</li>
      </ul>
    </div>
    <p class="ghost-mark">KTW Electrical and Data</p>
    <div class="contact-row">
      <svg width="14" height="14" viewBox="0 0 14 14" aria-hidden="true">
        <circle cx="7" cy="7" r="7" fill="var(--orange)"/>
        <path d="M4.4 3.6l1.3-.3.8 1.8-.9.7c.4.9 1.1 1.6 2 2l.7-.9 1.8.8-.3 1.3c-3.1.2-5.6-2.3-5.4-5.4z" fill="#111"/>
      </svg>
      <span class="contact-row__phone">0418 362 927</span>
      <span class="contact-row__divider"></span>
      <span class="contact-row__web">website-ktwelec.example.com.au</span>
    </div>
  </section>

  <section class="card card--front" aria-label="Card front">
    <div class="brand">
      <span class="brand__dot"></span>
      <span class="brand__name">KTW Electrical and Data</span>
    </div>
  </section>

</body>
</html>
```